Build a Website for TorvenGroup

TorvenGroup in Los Angeles CA USA needs a new website. Spanish/English

The law firm has strong ties to the Hispanic community. Former politician and City District Attorney.

This is not a static website, the platform you use when creating the site, is important, SEO is key, and how easy we can update as well.
This will be a very busy site. We will be updating weekly, posting press releases, court orders, articles, and more... It will also have a resource page for links and forms, a education or learning page, a self help help page for forms and briefings,
Please comment on your entry what features can be included and considered.

Services offered
Litigation
Bankruptcy
Real Estate Law
Foreclosure Defense
Loan Origination Fraud
Unlawful Detainer
DUI
Immigration
Elder Abuse
Personal Injury

Liked law sites
http://marnetolvaylaw.example/
http://www.dreckfinnow.example.au/
http://www.perdomaxlin.example/
http://www.quorvainjurylaw.example/
http://www.trevanique.example
http://kdfirm.example/
http://hollowick-law.example/

Create a new website that will have a structure designed to integrate the different evolution of needs for the TorvenGroup and clients alike.

Also analyzing legal websites rankings based on traffic and referrals.

Some general ideas are:

A) A communication section which includes news, bulletins, statistics provided by regulators, courts, government, news organizations, and our own. The
content is selected for the purpose of educating and informing what is happening, what we are doing and how we contribute to the solution. This is the most active section where TorvenGroup's P.R., press releases will be published, as well as court cases, news editorials, reviews, clients testimonials and more.

B) TorvenGroup's presentation section will introduce The Team, Resume, bios, contact, and personal experience of each member.

C) An Advertisement and Promotions section. Heavily linked and integrated with the media and communication for the purpose of lead generation, consultation, could include Q&A, Video vault, commercials, presentations and more.

D) A Self Help section which will provide many legal forms, free eBooks that explain services, or provide general information. List of Docs needed for the
Intake as well as most needed for others.

E) Draft the Privacy Policy, Terms and Conditions, Disclosures, Partner and Providers Acknowledgements. Resources, Useful Links, and other general Info

Please consider, This is not a static website, the platform you use when creating the site, is important, SEO is key, and how easy we can update as well.
This will be a very busy site. We will be updating weekly, posting press releases, court orders, articles, and more... It will also have a resource page for links and forms, a education or learning page, a self help help page for forms and more

Please!!! Add in the comments with your design, what customization will you do If awarded. And what features are included. I hope nobody is thinking to win $640 for a template, no matter how pretty or exclusive. We all know what templates go for and many of them include lots of programming...

Thanks a bunch

```html
<!DOCTYPE html>
<html lang="en">
<head>
<meta charset="utf-8">
<title>TorvenGroup</title>
<link rel="stylesheet" href="https://fonts.googleapis.com/css2?family=Cuprum:wght@400;700&family=Ubuntu:wght@400;500&display=swap">
<style>
:root{
  --sky:#a9d1f6;
  --page:#ececec;
  --panel:#f3f3f3;
  --white:#ffffff;
  --ink:#6e6e6e;
  --ink-soft:#8d8d8d;
  --heading:#4f7fae;
  --navy:#1d3f63;
  --accent-red:#c8283a;
  --link-blue:#2c6fb4;
  --rule:#d6d6d6;
  --field:#e0e0e0;
  --field-line:#cdcdcd;
  --wine:#5a0c12;
  --social:#1d4f9c;
}
*{box-sizing:border-box;margin:0;padding:0}
html,body{width:1051px;height:1200px;overflow:hidden}
body{background:var(--sky);font-family:'Ubuntu',sans-serif;color:var(--ink);position:relative}
.page{position:absolute;left:149px;top:0;width:752px;height:1200px;background:var(--page);box-shadow:0 0 6px rgba(0,0,0,.15)}
.abs{position:absolute}

/* header */
.phone-box{left:359px;top:21px;width:329px;height:28px;background:#dedede;border:1px solid #cfcfcf;display:flex;align-items:center;padding-left:8px;gap:8px;font-family:'Cuprum',sans-serif;color:var(--navy)}
.phone-box small{font-size:11px}
.phone-box strong{font-size:19px;font-weight:400}
.nav-band{left:11px;top:68px;width:731px;height:40px;background:var(--white);box-shadow:0 2px 3px rgba(0,0,0,.12)}
.logo-tab{left:0;top:60px;width:260px;height:90px;z-index:2}
.brand{left:78px;top:108px;display:flex;align-items:center;gap:6px;font-family:'Cuprum',sans-serif;font-size:16px;line-height:18px;color:var(--link-blue);z-index:3}
.brand i{display:block;width:11px;height:11px;background:var(--link-blue)}
.nav{left:295px;top:80px;display:flex;font-family:'Cuprum',sans-serif;font-size:14px;color:var(--navy)}
.nav a{text-decoration:none;color:inherit;margin-right:28px}
.nav a.current{color:var(--accent-red)}

/* hero */
.hero{left:11px;top:107px;width:731px;height:228px;background:linear-gradient(100deg,#3c4f78 0%,#9b4a4a 30%,#c8a08a 50%,#6a3a20 68%,#b88a3a 80%,#4a2a18 100%)}
.hero-text{font-family:'Cuprum',sans-serif;color:rgba(255,255,255,.75);text-shadow:0 1px 3px rgba(0,0,0,.5);white-space:nowrap}
.hero-small-1{left:90px;top:167px;font-size:19px}
.hero-big{left:157px;top:191px;font-size:44px;font-weight:700;color:#1e86d8;text-shadow:0 2px 4px rgba(0,0,0,.6)}
.hero-small-2{left:309px;top:242px;font-size:19px}

/* feature boxes */
.feature{background:var(--white);border-radius:4px;box-shadow:0 1px 3px rgba(0,0,0,.12)}
.feature h3{font-family:'Cuprum',sans-serif;font-weight:400;font-size:14px;color:var(--heading);line-height:17px;margin-bottom:1px}
.feature p{font-size:8.5px;line-height:17px;color:var(--ink);white-space:nowrap}
.read-more{font-family:'Cuprum',sans-serif;font-size:10px}
.field{width:175px;height:15px;background:var(--field);border:1px solid var(--field-line);font-size:8.5px;color:var(--ink-soft);padding-left:5px;line-height:13px;margin-bottom:6px}

/* main panel */
.main{left:24px;top:506px;width:703px;height:633px;background:var(--panel);border-radius:4px;box-shadow:inset 0 8px 10px -6px rgba(0,0,0,.12)}
.tab-head{display:flex;align-items:flex-end}
.tab-head span{font-family:'Cuprum',sans-serif;font-size:14px;color:var(--heading);padding:3px 12px 2px 12px;background:#f8f8f8;border:1px solid var(--rule);border-bottom:none;border-radius:4px 14px 0 0}
.tab-head b{flex:1;border-bottom:1px solid var(--rule);height:1px}
.body-text{font-size:9px;line-height:17px;color:var(--ink)}
.staff-photo{width:112px;height:112px;border-radius:50%;border:4px solid #fff;box-shadow:0 1px 4px rgba(0,0,0,.3)}
.staff-name{font-size:9px;color:#6a6a6a;text-align:center;width:140px}
.staff-role{font-family:'Cuprum',sans-serif;font-size:13px;color:#5d5d5d;text-align:center;width:140px}
.services{list-style:none}
.services li{height:29.5px;border-bottom:1px solid var(--rule);display:flex;align-items:center;gap:12px;font-size:8.5px;text-transform:uppercase;color:#7a7a7a;padding-left:6px}
.services li.active{color:#4b8fd0}
.services svg{width:14px;height:14px;flex:none}
.client-avatar{float:left;width:36px;height:36px;margin:0 8px 2px 0;border-radius:50%;border:2px solid #fff;background:radial-gradient(circle,#c9a68a,#5a4436);box-shadow:0 1px 3px rgba(0,0,0,.3)}
.footer{font-size:9px;color:var(--ink-soft)}
</style>
</head>
<body>
<div class="page">

  <!-- header -->
  <div class="abs phone-box"><small>Call us today for free case evolution</small><strong>(555)-000-482913</strong></div>

  <div class="abs nav-band"></div>
  <nav class="abs nav">
    <a class="current" href="#">Home</a>
    <a href="#">About Us</a>
    <a href="#">Practise Area</a>
    <a href="#">Case Example</a>
    <a href="#">Faqs</a>
    <a href="#" style="margin-right:0">Contact Us</a>
  </nav>

  <!-- hero -->
  <div class="abs hero" role="img" aria-label="Banner photo: a flag, a gavel and a golden statue of Justice holding scales"></div>
  <div class="abs hero-text hero-small-1">TorvenGroup</div>
  <div class="abs hero-text hero-big">TorvenGroup</div>
  <div class="abs hero-text hero-small-2">TorvenGroup</div>

  <svg class="abs logo-tab" viewBox="0 0 260 90" aria-hidden="true">
    <path d="M11 8 H246 V47 C214 50 196 82 138 82 C78 82 34 66 11 46 Z" fill="#ffffff"/>
  </svg>
  <div class="abs brand"><i></i>TorvenGroup</div>

  <!-- feature boxes -->
  <div class="abs feature" style="left:25px;top:347px;width:201px;height:108px">
    <div class="abs" style="left:11px;top:9px;width:140px">
      <h3>Case Example &amp;<br>Result</h3>
      <p>Lorem ipsum dolor sit amet,<br>con tetur adipiscing elit. Duis<br>vel nifes. Vestibul ullam corper<br>dolor mole dio sed tincidunt</p>
    </div>
    <div class="abs" style="left:156px;top:36px;width:1px;height:50px;background:var(--rule)"></div>
    <svg class="abs" style="left:163px;top:38px" width="34" height="34" viewBox="0 0 34 34" aria-hidden="true">
      <g transform="rotate(-18 17 17)"><rect x="4" y="10" width="26" height="18" rx="2" fill="#1b1b1b"/><rect x="12" y="6" width="10" height="6" rx="1.5" fill="none" stroke="#1b1b1b" stroke-width="2"/></g>
    </svg>
  </div>
  <div class="abs read-more" style="left:118px;top:474px;color:var(--accent-red)">Read More..</div>

  <div class="abs feature" style="left:276px;top:347px;width:201px;height:108px">
    <div class="abs" style="left:11px;top:9px;width:145px">
      <h3>Quick Information<br>Center</h3>
      <p>Lorem ipsum dolor sit amet,<br>con tetur adipiscing elit. Duis<br>vel nifes. Vestibul ullam corper<br>dolor mole dio sed tincidunt</p>
    </div>
    <div class="abs" style="left:161px;top:36px;width:1px;height:50px;background:var(--rule)"></div>
    <svg class="abs" style="left:166px;top:40px" width="32" height="28" viewBox="0 0 32 28" aria-hidden="true">
      <g transform="rotate(-20 16 14)" fill="#fff" stroke="#222" stroke-width="1.6"><rect x="3" y="6" width="26" height="16"/><path d="M3 6 L16 16 L29 6"/></g>
    </svg>
  </div>
  <div class="abs read-more" style="left:429px;top:474px;color:var(--link-blue)">Read More..</div>

  <div class="abs feature" style="left:521px;top:347px;width:201px;height:143px">
    <h3 class="abs" style="left:16px;top:6px">Quick Contact</h3>
    <div class="abs" style="left:15px;top:28px">
      <div class="field">Name</div>
      <div class="field">Email</div>
      <div class="field">Phone Number</div>
      <div class="field" style="height:30px">Message</div>
    </div>
    <div class="abs read-more" style="left:150px;top:126px;color:var(--link-blue)">Send Now</div>
  </div>

  <!-- main panel -->
  <div class="abs main">
    <div class="abs tab-head" style="left:14px;top:17px;width:440px"><span>About Company</span><b></b></div>
    <div class="abs body-text" style="left:13px;top:47px;width:445px">
      <p>Praesent vestibulum molestie nonumm erit mais. Phasellu por fusce smium soina pen et manirtu riennes nasetur memo lestie lacuanulla dui. Fusce feug male suada odio. Morbi nuncod gridem dolore secenas.</p>
      <p style="margin-top:17px">Phasellu por fusce smium soina penati et manirtu riennes nasetur memo lestie lacuan ulla dui. Fusce feug male suada odio. Morbi nuncod gridem dolore secenas.</p>
      <p style="margin-top:17px">Phasellu por fusce smium soina penati et manirtu riennes nasetur memo lestie lacuan ulla dui. Fusce feug male suada odio. Morbi nuncod gridem dolore secenas.</p>
    </div>

    <div class="abs tab-head" style="left:14px;top:217px;width:440px"><span>Our Staff</span><b></b></div>
    <svg class="abs" style="left:14px;top:300px" width="14" height="14" viewBox="0 0 14 14" aria-hidden="true"><path d="M11 1 L3 7 L11 13 Z" fill="#9a9a9a"/></svg>
    <svg class="abs" style="left:443px;top:300px" width="14" height="14" viewBox="0 0 14 14" aria-hidden="true"><path d="M3 1 L11 7 L3 13 Z" fill="#9a9a9a"/></svg>

    <div class="abs staff-photo" style="left:43px;top:251px;background:radial-gradient(circle at 50% 40%,#d9b79c,#6b4f3f 75%)" role="img" aria-label="Portrait of a criminal advocate"></div>
    <div class="abs staff-photo" style="left:179px;top:251px;background:radial-gradient(circle at 50% 40%,#8a5a3e,#2e2622 75%)" role="img" aria-label="Portrait of a family lawyer"></div>
    <div class="abs staff-photo" style="left:315px;top:251px;background:radial-gradient(circle at 50% 40%,#e8c6ac,#6f4a34 75%)" role="img" aria-label="Portrait of an employment advocate"></div>

    <div class="abs staff-name" style="left:29px;top:378px">Mr. Name here</div>
    <div class="abs staff-role" style="left:29px;top:392px">Criminal Advocate</div>
    <div class="abs staff-name" style="left:165px;top:378px">Mr. Name here</div>
    <div class="abs staff-role" style="left:165px;top:392px">Family Lawyer</div>
    <div class="abs staff-name" style="left:301px;top:378px">Mrs. Name here</div>
    <div class="abs staff-role" style="left:301px;top:392px">Employment&nbsp; Advocate</div>

    <div class="abs tab-head" style="left:14px;top:462px;width:205px"><span>Client's Speak</span><b></b></div>
    <div class="abs body-text" style="left:12px;top:499px;width:205px">
      <div class="client-avatar" role="img" aria-label="Client portrait"></div>
      “ Nulla placerat gravida risus in tempus. Ut eu mi nibh,<br>at rutrum eros. Integer a mollis magna. Phasellus ut pharetra... ”
    </div>
    <div class="abs" style="left:123px;top:575px;font-size:10px;font-style:italic;color:var(--accent-red)">Dalven Ostrik</div>

    <div class="abs" style="left:225px;top:490px;width:1px;height:110px;background:linear-gradient(#f3f3f3,#d8d8d8,#f3f3f3)"></div>

    <div class="abs tab-head" style="left:248px;top:462px;width:210px"><span>Lastest News</span><b></b></div>
    <div class="abs body-text" style="left:247px;top:496px;width:212px">Praesent vestibulum molestie nonumm erit mais. Phasellu por fusce smium soina pen et manirtu riennes nasetur memo lestie lacuanulla dui. Fusce feug male suada odio. Morbi nuncod gridem dolore secenas.</div>

    <div class="abs" style="left:470px;top:10px;width:1px;height:610px;background:linear-gradient(#f3f3f3,#dcdcdc 20%,#dcdcdc 80%,#f3f3f3)"></div>

    <!-- services -->
    <div class="abs tab-head" style="left:496px;top:17px;width:205px"><span>Services</span><b></b></div>
    <ul class="abs services" style="left:496px;top:41px;width:179px">
      <li class="active"><svg viewBox="0 0 14 14"><rect x="6" y="1" width="2" height="12" fill="#4b8fd0"/></svg>Wills &amp; Estates</li>
      <li><svg viewBox="0 0 14 14"><g fill="#8a8a8a"><rect x="1" y="5" width="2" height="8"/><rect x="4.5" y="3" width="2" height="10"/><rect x="8" y="4" width="2" height="9"/><rect x="11.5" y="6" width="2" height="7"/></g></svg>Family Law</li>
      <li><svg viewBox="0 0 14 14"><path d="M2 2 L12 12 M12 2 L2 12" stroke="#8a8a8a" stroke-width="2"/></svg>Employment Law</li>
      <li><svg viewBox="0 0 14 14"><path d="M1 12 L5 5 L8 9 L10 6 L13 12 Z" fill="#8a8a8a"/></svg>Succession Law</li>
      <li><svg viewBox="0 0 14 14"><path d="M1 7 L7 2 L13 7 H11 V12 H3 V7 Z" fill="#8a8a8a"/></svg>Conveyancing</li>
      <li><svg viewBox="0 0 14 14"><g fill="none" stroke="#8a8a8a" stroke-width="1.6"><circle cx="4.5" cy="7" r="3"/><circle cx="10" cy="7" r="3"/></g></svg>Criminal Law</li>
      <li><svg viewBox="0 0 14 14"><path d="M1 12 L7 3 L13 12 M4 9 H10" stroke="#8a8a8a" stroke-width="1.6" fill="none"/></svg>Litigation</li>
    </ul>

    <div class="abs tab-head" style="left:496px;top:270px;width:207px"><span>Helpfull Video</span><b></b></div>
    <div class="abs" style="left:493px;top:309px;width:210px;height:143px;background:linear-gradient(#6f7c8a,#c9ccd0 55%,#8b8d90);box-shadow:0 1px 3px rgba(0,0,0,.3)" role="img" aria-label="Video still of a building front with a flag"></div>
    <svg class="abs" style="left:493px;top:309px" width="210" height="143" viewBox="0 0 210 143" aria-hidden="true">
      <circle cx="105" cy="62" r="30" fill="rgba(255,255,255,.25)" stroke="#fff" stroke-width="3"/>
      <path d="M96 46 L120 62 L96 78 Z" fill="#fff"/>
      <rect x="0" y="129" width="210" height="14" fill="#1a1a1a"/>
      <rect x="5" y="133" width="3" height="6" fill="#ddd"/><rect x="10" y="133" width="3" height="6" fill="#ddd"/>
      <rect x="40" y="135" width="140" height="2" fill="#555"/><rect x="40" y="135" width="12" height="2" fill="#ddd"/>
      <text x="22" y="139" font-size="6" fill="#ccc" font-family="Ubuntu, sans-serif">00:18</text>
      <text x="188" y="139" font-size="6" fill="#ccc" font-family="Ubuntu, sans-serif">01:38</text>
    </svg>

    <div class="abs" style="left:493px;top:469px;width:210px;height:97px;border-radius:4px;background:linear-gradient(90deg,#3d0509,var(--wine) 50%,#7a1a1a);box-shadow:0 1px 3px rgba(0,0,0,.35)"></div>
    <div class="abs" style="left:600px;top:476px;width:96px;height:84px;border-radius:4px;background:radial-gradient(circle,#b78a2e,rgba(90,12,18,0) 70%)" role="img" aria-label="Golden scales of justice"></div>
    <div class="abs" style="left:493px;top:506px;width:100px;text-align:center;font-family:'Cuprum',sans-serif;font-size:13px;line-height:18px;color:#fff">Donlwoad e-books<br>&amp; forms</div>

    <div class="abs" style="left:493px;top:582px;width:210px;height:40px;border-radius:3px;background:linear-gradient(var(--social),#163d7c);box-shadow:0 1px 3px rgba(0,0,0,.35)"></div>
    <div class="abs" style="left:553px;top:592px;width:22px;height:22px;border-radius:3px;background:#2f6bc0;border:1px solid #6e9bdc"></div>
    <div class="abs" style="left:594px;top:592px;width:22px;height:22px;border-radius:3px;background:#2f6bc0;border:1px solid #6e9bdc"></div>
    <div class="abs" style="left:635px;top:592px;width:22px;height:22px;border-radius:3px;background:#2f6bc0;border:1px solid #6e9bdc"></div>
  </div>

  <div class="abs" style="left:11px;top:1139px;width:731px;height:14px;background:radial-gradient(ellipse at top,rgba(0,0,0,.12),rgba(0,0,0,0) 70%)"></div>

  <!-- footer -->
  <div class="abs footer" style="left:18px;top:1175px">© TorvenGroup 2013. All Rights Reserved.</div>
  <div class="abs footer" style="left:595px;top:1175px">Legal Information&nbsp; | &nbsp;Privacy Policy</div>
</div>
</body>
</html>
```